Red Gum Business Card Design

We are a new small business specialising in under ground cable jointing and excavation works in NSW Australia.
Design I'm looking for is incorporating the Australian flag & excavator with out being to cheesy.
Maybe a faded washed out flag to help with overload of colour? & so its not the main focus.
Very open to creative out of the box designs!

Target Market(s)

Building & Construction

Industry/Entity Type

Construction

Contact Information for Business Card

Red Gum Cable Jointing & Excavations
Owen Falkirk

Ph: 0438 605 312
E: owen.falkirk@tallmail.example

Reverse Side
Services we offer:
High Voltage & Low Voltage Cable Jointing
Polymeric & paperlead jointing & terminations
Trenching & Auger Drilling 150 - 600mm
Site preparation / leveling / clearing
Driveway / Footpath / Turf Prep
Rubbish Removal
Tree & Stump removal
Footings & Post holes
Drainage
Service Installs
Gravels & Sands available
Any general Earth moving needs
Reliable Free Quotes
Fully Insured

Font styles to use
Serif
Script

Requirements
Nice to have
• small excavator (See uploaded picture)

```html
<!DOCTYPE html>
<html lang="en">
<head>
<meta charset="utf-8">
<title>Red Gum Business Card Design</title>
<link href="https://fonts.googleapis.com/css2?family=Archivo+Black&family=Didact+Gothic&family=Lato:ital@1&family=Oswald:wght@400&display=swap" rel="stylesheet">
<style>
  :root {
    --navy: #283371;
    --red: #e0203c;
    --white: #ffffff;
    --page: #e9e9ec;
    --flag-soft: #8f9bc8;
  }
  * { box-sizing: border-box; margin: 0; padding: 0; }
  html, body { width: 1200px; height: 862px; overflow: hidden; }
  body {
    background: var(--page);
    display: flex;
    align-items: center;
    justify-content: center;
    gap: 70px;
  }
  .card {
    position: relative;
    width: 340px;
    height: 580px;
    box-shadow: 0 10px 30px rgba(0,0,0,0.18);
    overflow: hidden;
  }

  /* Reverse side */
  .card--services { background: var(--navy); color: var(--white); }
  .card--services .edge-strip {
    position: absolute; top: 0; right: 0; width: 22px; height: 100%;
    background: var(--red);
  }
  .card--services .guide-line {
    position: absolute; top: 0; bottom: 0; left: 26px; width: 2px;
    background: var(--white);
  }
  .service-list {
    position: absolute; left: 46px; right: 40px;
    list-style: none;
    font-family: "Lato", sans-serif; font-style: italic;
    font-size: 13px; line-height: 24px;
  }
  .service-list--upper { top: 36px; }
  .service-list--lower { top: 370px; }
  .services-band {
    position: absolute; left: 0; right: 22px; top: 262px; height: 66px;
    border-top: 2px solid var(--white);
    border-bottom: 2px solid var(--white);
    display: flex; align-items: center;
  }
  .services-band h2 {
    font-family: "Oswald", sans-serif; font-weight: 400;
    font-size: 17px; letter-spacing: 1px;
    margin-left: 30px;
  }
  .services-band .map-art {
    position: absolute; right: 14px; top: -8px;
    width: 110px; height: 86px; border-radius: 40% 45% 38% 50%;
    background: linear-gradient(135deg, var(--white), var(--flag-soft));
  }

  /* Front side */
  .card--contact { background: var(--white); color: var(--navy); }
  .badge {
    position: absolute; width: 52px; height: 52px;
    border: 1.5px solid var(--navy); border-radius: 50%;
    display: flex; align-items: center; justify-content: center;
  }
  .badge .badge-art {
    width: 38px; height: 38px; border-radius: 50%;
    background: linear-gradient(135deg, var(--navy), var(--flag-soft));
  }
  .badge--top { top: 70px; left: 22px; }
  .badge--bottom { bottom: 70px; right: 22px; }
  .rule { position: absolute; height: 2px; background: var(--navy); }
  .rule--top { top: 95px; left: 74px; right: 0; }
  .rule--bottom { bottom: 95px; left: 0; right: 74px; }
  .contact-block {
    position: absolute; top: 200px; left: 0; right: 0;
    text-align: center;
  }
  .business-name {
    font-family: "Archivo Black", sans-serif;
    font-size: 28px; line-height: 1.1;
  }
  .business-tagline {
    font-family: "Didact Gothic", sans-serif;
    font-size: 17px; letter-spacing: 2px; margin-top: 4px;
  }
  .person-name {
    font-family: "Archivo Black", sans-serif;
    font-size: 18px; margin-top: 16px;
  }
  .contact-detail {
    font-family: "Didact Gothic", sans-serif;
    font-size: 15px; letter-spacing: 1.5px; margin-top: 8px;
  }
  .contact-detail + .contact-detail { margin-top: 2px; }
</style>
</head>
<body>
  <section class="card card--services" aria-label="Reverse side">
    <div class="guide-line"></div>
    <div class="edge-strip"></div>
    <ul class="service-list service-list--upper">
      <li>Footings &amp; Post holes</li>
      <li>Drainage</li>
      <li>Service Installs</li>
      <li>Gravels &amp; Sands available</li>
      <li>Any general Earth moving needs</li>
      <li>Reliable Free Quotes</li>
      <li>Fully Insured</li>
    </ul>
    <div class="services-band">
      <h2>SERVICES WE OFFER</h2>
      <div class="map-art" role="img" aria-label="Map of Australia filled with the Australian flag"></div>
    </div>
    <ul class="service-list service-list--lower">
      <li>Driveway / Footpath / Turf Prep</li>
      <li>Rubbish Removal</li>
      <li>Tree &amp; Stump removal</li>
      <li>High Voltage &amp; Low Voltage Cable Jointing</li>
      <li>Polymeric &amp; paperlead jointing &amp; terminations</li>
      <li>Trenching &amp; Auger Drilling 150 - 600mm</li>
      <li>Site preparation / leveling / clearing</li>
    </ul>
  </section>

  <section class="card card--contact" aria-label="Front side">
    <div class="badge badge--top"><div class="badge-art" role="img" aria-label="Small map of Australia with the flag"></div></div>
    <div class="rule rule--top"></div>
    <div class="contact-block">
      <h1 class="business-name">Red Gum Cable</h1>
      <p class="business-tagline">Jointing &amp; Excavations</p>
      <p class="person-name">Owen Falkirk</p>
      <p class="contact-detail">0438 605 312</p>
      <p class="contact-detail">owen.falkirk@tallmail.example</p>
    </div>
    <div class="rule rule--bottom"></div>
    <div class="badge badge--bottom"><div class="badge-art" role="img" aria-label="Small excavator icon"></div></div>
  </section>
</body>
</html>
```